Book a Belle needs a Stunning web design

Book a Belle is an upmarket agency in Sydney that has lingerie waitresses for events.

Book a Belle is looking for a website design that is as sexy and sophisticated as the ladies who work for them!

The design mustn't be cluttered, tacky or pornographic. What I'm looking for is something better than the industry leader www.velvetgrace.com.au Something classy, sexy and different.

When designing please suggest a CMS, we already use wordpress but are open to suggestions.

We will need a home page that incorporates a feed from a blog and/or social media (please make suggestions and use your discretion as a designer, however we'd like to approve what goes into the feed before it goes in.) The home page could also have a list of our services, but if not we will need a services page. Our Services include:
Lingerie waitressing at events
Lingerie waitresses to help dress the groom pre wedding.
Bucks parties

We have a logo that we'd like incorporated into the design and have attached it.

We will also need a portfolio page for the ladies, This is not to be cluttered, tacky or pornographic. It needs to be classy.

We will also need a "Contact us" page and were thinking that this could potentially also be a "Ask for a quote on your event" page. I.e. have a regular "Contact us" form but have alternate fields if they tick the "I want a quote" box. Alternatively you could have two parts to the contact us page. One that is a regular form and one that has a "Your requirements" box.

Again please use your discretion when designing these, if it's too cluttered it won't work. If it looks tacky, don't do it. If you have suggestions make them.

Target Market(s)

Males between the ages of 18 - 45

Industry/Entity Type

Industry

Requirements
Must have
• Must incorporate our logo.

```html
<!DOCTYPE html>
<html lang="en">
<head>
<meta charset="utf-8">
<title>Book a Belle</title>
<link rel="stylesheet" href="https://fonts.googleapis.com/css2?family=Crimson+Text:ital@0;1&family=Libre+Baskerville:wght@400;700&family=Questrial&family=Tinos&family=Oswald:wght@300&display=swap">
<style>
:root{
  --black:#050505;
  --gold:#b8862e;
  --gold-band:#b9912f;
  --blush:#ede3df;
  --ink:#1a1a1a;
  --footer:#1e1c1b;
  --footer-muted:#6f6a64;
  --rule:#d6d0cc;
  --white:#ffffff;
}
*{margin:0;padding:0;box-sizing:border-box}
html,body{width:997px;height:1200px;overflow:hidden;background:var(--blush)}
body{position:relative;font-family:"Tinos",serif;color:var(--ink)}
.abs{position:absolute}
.topbar{left:0;top:0;width:997px;height:27px;background:var(--black)}
.search{left:662px;top:14px;width:190px;height:17px;background:#d8d8d8;border:1px solid #aaa;font:8px "Questrial",sans-serif;color:#777;padding:3px 5px}
.search-btn{left:835px;top:14px;width:17px;height:17px;background:#d6b82a}
.hero{left:0;top:27px;width:997px;height:583px;
  background:
    radial-gradient(ellipse 260px 200px at 65% 30%,rgba(240,200,170,.75),rgba(240,200,170,0)),
    radial-gradient(ellipse 300px 170px at 35% 40%,rgba(250,228,200,.85),rgba(250,228,200,0)),
    radial-gradient(ellipse 180px 260px at 6% 30%,rgba(220,205,180,.9),rgba(220,205,180,0)),
    radial-gradient(ellipse 380px 240px at 55% 85%,rgba(205,150,140,.6),rgba(205,150,140,0)),
    linear-gradient(100deg,#5d3a55 0%,#7a5068 20%,#caa08c 45%,#b47c80 65%,#6a3a58 85%,#3e1e38 100%)}
.hero-fade{left:0;top:27px;width:997px;height:60px;background:linear-gradient(#c79f72,rgba(199,159,114,0))}
.gold-band{left:0;top:610px;width:997px;height:9px;background:var(--gold-band)}
.nav{left:139px;top:27px;width:106px;height:201px;background:linear-gradient(#111 40%,#555);border-radius:0 0 4px 4px;text-align:center}
.brand{display:block;margin-top:26px;font:400 13px "Libre Baskerville",serif;color:var(--gold);white-space:nowrap}
.nav ul{list-style:none;margin-top:22px}
.nav li{font:11px "Questrial",sans-serif;color:var(--gold);letter-spacing:.5px;line-height:23px;border-top:1px solid #8a6a2c;margin:0 12px}
.nav li:last-child{border-bottom:1px solid #8a6a2c}
.card{background:var(--white)}
.card-left{left:100px;top:431px;width:237px;height:417px}
.card-left-bar{left:100px;top:845px;width:237px;height:5px;background:#1b1b1b}
.feature-photo{left:111px;top:442px;width:214px;height:322px;
  background:
    radial-gradient(ellipse 70px 120px at 55% 50%,rgba(235,170,130,.85),rgba(235,170,130,0)),
    radial-gradient(ellipse 60px 40px at 50% 36%,rgba(190,60,140,.7),rgba(190,60,140,0)),
    radial-gradient(ellipse 60px 30px at 55% 78%,rgba(190,60,140,.6),rgba(190,60,140,0)),
    linear-gradient(160deg,#3a5040 0%,#7a6a40 30%,#c8865e 55%,#8e7a5a 80%,#5e6a58 100%)}
.thumb{top:780px;width:48px;height:49px}
.social-head{left:100px;top:880px;width:237px;text-align:center;font:italic 15px "Crimson Text",serif;color:#333}
.quote{left:106px;top:913px;width:224px;text-align:center;font:italic 10.5px/17.5px "Crimson Text",serif;color:#333}
.social-brand{left:111px;top:983px;font:400 13px "Libre Baskerville",serif;color:var(--gold)}
.social-link{left:214px;top:978px;font:9px "Questrial",sans-serif;color:#3b5998}
.like{left:214px;top:995px;width:35px;height:14px;border:1px solid #bbb;background:#f3f3f3;font:8px "Questrial",sans-serif;color:#333;padding-left:16px;line-height:12px}
.like::before{content:"";position:absolute;left:3px;top:2px;width:9px;height:9px;background:#4a66a0}
.like-count{left:254px;top:995px;width:23px;height:14px;border:1px solid #bbb;background:#fff;font:8px "Questrial",sans-serif;text-align:center;line-height:12px}
.card-main{left:351px;top:431px;width:545px;height:485px;box-shadow:0 0 3px rgba(0,0,0,.08)}
.title{left:370px;top:455px;font:32px "Crimson Text",serif;color:var(--gold);font-weight:400}
.title-rule{left:543px;top:478px;width:339px;height:1px;background:var(--rule)}
.intro{left:370px;top:500px;width:490px;font:13px/20px "Tinos",serif}
.avail{left:370px;top:560px;font:13px "Tinos",serif}
.book{left:373px;top:607px;width:105px;height:28px;background:var(--black);color:#fff;font:13px "Tinos",serif;line-height:28px;padding-left:15px}
.book svg{position:absolute;right:9px;top:9px}
.girls-title{left:373px;top:664px;font:18px "Crimson Text",serif;font-weight:400}
.girls-rule{left:455px;top:679px;width:420px;height:1px;background:var(--rule)}
.cat{top:714px;width:84px;font:300 9px/12px "Oswald",sans-serif;color:var(--gold);text-transform:uppercase}
.cat svg{position:absolute;right:0;top:2px}
.cat-photo{top:748px;width:84px;height:118px}
.gold-line{left:0;top:1018px;width:997px;height:5px;background:var(--gold-band)}
.footer{left:0;top:1023px;width:997px;height:177px;background:var(--footer)}
.foot-head{top:1046px;font:700 9px "Libre Baskerville",serif;color:var(--footer-muted);text-transform:uppercase}
.foot-head svg{position:absolute;left:-16px;top:1px}
.foot-list{top:1068px;list-style:none;font:700 9.5px/19px "Libre Baskerville",serif;color:#fff}
.copyright{left:0;top:1182px;width:997px;text-align:center;font:9px "Libre Baskerville",serif;color:#4d4944}
</style>
</head>
<body>
<div class="abs topbar"></div>
<div class="abs hero" role="img" aria-label="Hero photograph of a model in lingerie reclining in a warm-lit bedroom"></div>
<div class="abs hero-fade"></div>
<div class="abs search">Search...</div>
<div class="abs search-btn"></div>
<nav class="abs nav">
  <span class="brand">Book a Belle</span>
  <ul><li>home</li><li>services</li><li>portfolio</li><li>contact us</li></ul>
</nav>
<div class="abs gold-band"></div>

<div class="abs card card-left"></div>
<div class="abs feature-photo" role="img" aria-label="Featured model portrait in a pink bikini by a poolside"></div>
<div class="abs thumb" style="left:111px;background:radial-gradient(circle at 55% 45%,#d9a07e,#7a4a36 70%)" role="img" aria-label="Gallery thumbnail"></div>
<div class="abs thumb" style="left:166px;background:radial-gradient(circle at 50% 45%,#c98a6a,#3c4a2e 75%)" role="img" aria-label="Gallery thumbnail"></div>
<div class="abs thumb" style="left:221px;background:radial-gradient(circle at 50% 55%,#d58a8e,#5c6a4a 75%)" role="img" aria-label="Gallery thumbnail"></div>
<div class="abs thumb" style="left:276px;background:radial-gradient(circle at 50% 50%,#c87a8a,#6a7058 75%)" role="img" aria-label="Gallery thumbnail"></div>
<div class="abs card-left-bar"></div>

<div class="abs social-head">Belle Staffing @ Socialpage</div>
<p class="abs quote">"We had a great night, we were really impressed with the options and service at such late notice. Thank you! We will use Boutique Belles again"</p>
<div class="abs social-brand">Book a Belle</div>
<div class="abs social-link">on Socialpage</div>
<div class="abs like">Like</div>
<div class="abs like-count">1.8k</div>

<div class="abs card card-main"></div>
<h1 class="abs title">Lorem Xoxo</h1>
<div class="abs title-rule"></div>
<p class="abs intro">Lorem ipsum dolor sit amet, consectetur adipiscing elit. Etiam sed consequat massa.<br>Curabitur rutrum libero ultricies mi adipiscing feugiat.</p>
<p class="abs avail">Available-Most days, with notice.</p>
<div class="abs book">Book Now<svg width="10" height="10" viewBox="0 0 10 10"><path d="M0 5h8M5 1l4 4-4 4" stroke="#fff" stroke-width="1.6" fill="none"/></svg></div>
<h2 class="abs girls-title">Our Girls</h2>
<div class="abs girls-rule"></div>

<div class="abs cat" style="left:373px">Promo<br>Models<svg width="8" height="8" viewBox="0 0 10 10"><path d="M0 5h8M5 1l4 4-4 4" stroke="#111" stroke-width="1.6" fill="none"/></svg></div>
<div class="abs cat" style="left:474px">Lingerie<br>Models<svg width="8" height="8" viewBox="0 0 10 10"><path d="M0 5h8M5 1l4 4-4 4" stroke="#111" stroke-width="1.6" fill="none"/></svg></div>
<div class="abs cat" style="left:574px">Topless<br>Waitresses<svg width="8" height="8" viewBox="0 0 10 10"><path d="M0 5h8M5 1l4 4-4 4" stroke="#111" stroke-width="1.6" fill="none"/></svg></div>
<div class="abs cat" style="left:675px">Burlesque<br>Babes<svg width="8" height="8" viewBox="0 0 10 10"><path d="M0 5h8M5 1l4 4-4 4" stroke="#111" stroke-width="1.6" fill="none"/></svg></div>
<div class="abs cat" style="left:775px">Show Girls<svg width="8" height="8" viewBox="0 0 10 10"><path d="M0 5h8M5 1l4 4-4 4" stroke="#111" stroke-width="1.6" fill="none"/></svg></div>

<div class="abs cat-photo" style="left:373px;background:radial-gradient(ellipse 30px 50px at 50% 55%,#2a2a2e,rgba(42,42,46,0)),linear-gradient(#c3ced6,#8a96a0 60%,#4a4e56)" role="img" aria-label="Promo model photo"></div>
<div class="abs cat-photo" style="left:474px;background:radial-gradient(ellipse 32px 55px at 50% 50%,#e0c49a,rgba(224,196,154,0)),linear-gradient(90deg,#3a3634,#8a8480 50%,#3a3634)" role="img" aria-label="Lingerie model photo"></div>
<div class="abs cat-photo" style="left:574px;background:radial-gradient(ellipse 30px 50px at 55% 45%,#e0a47a,rgba(224,164,122,0)),linear-gradient(#7a8a5a,#3b88b8 65%,#b04040)" role="img" aria-label="Topless waitress category photo"></div>
<div class="abs cat-photo" style="left:675px;background:radial-gradient(ellipse 30px 55px at 50% 50%,#9a9a9a,rgba(154,154,154,0)),linear-gradient(#141414,#2a2a2a)" role="img" aria-label="Burlesque performer photo in black and white"></div>
<div class="abs cat-photo" style="left:775px;background:radial-gradient(ellipse 45px 30px at 45% 70%,#d89a80,rgba(216,154,128,0)),linear-gradient(#e6a8d8,#ecd6d8 80%,#d8c8c4)" role="img" aria-label="Showgirl photo on a pink backdrop"></div>

<div class="abs gold-line"></div>
<footer class="abs footer"></footer>
<div class="abs foot-head" style="left:296px"><svg width="10" height="9" viewBox="0 0 10 10"><path d="M0 5h8M5 1l4 4-4 4" stroke="#fff" stroke-width="1.6" fill="none"/></svg>Services &amp; Prices</div>
<ul class="abs foot-list" style="left:296px"><li>Strippers</li><li>Nude Models</li><li>Promo Girls</li><li>Lingerie Waitress</li></ul>
<ul class="abs foot-list" style="left:462px;top:1067px"><li>Topless Waitress</li><li>Burlesque Girls</li><li>Showgirls</li><li>Hot Shows</li></ul>
<div class="abs foot-head" style="left:628px"><svg width="10" height="9" viewBox="0 0 10 10"><path d="M0 5h8M5 1l4 4-4 4" stroke="#fff" stroke-width="1.6" fill="none"/></svg>Helpful Links</div>
<ul class="abs foot-list" style="left:628px"><li>Rules</li><li>Contact Us</li><li>Employment</li><li>Privacy Policy</li><li>Terms &amp; Conditions</li><li>Articles</li></ul>
<div class="abs copyright">© Copyright 2011 Belle Staffing</div>
</body>
</html>
```